Business Card Design

We need a business card design for a new company based in Melbourne Australia. We are financial broker in finance industry. We provide a wide range of finance solutions to our clients including home loans, commercial loans, business facilities, car loans, equipment loans, invoice finance, etc. The company name is from director's personal name. We would like to have a new company logo that includes KT.

Industry/Entity Type

Business

Contact Information for Business Card

company name: KT & Co Finance Pty Ltd
person's name: Kenneth Tollard
role: Managing Director
Mobile: 0417 638 294
fax: 03 9561 2047
Email: kenneth.tollard@ktcofinance.example
Address: Suite 4/718 Marlow Avenue Ferndale East Vic 3187
Credit Licence No.: 382917

```html
<!DOCTYPE html>
<html lang="en">
<head>
<meta charset="utf-8">
<title>KT &amp; Co Finance Pty Ltd – Business Card</title>
<link rel="stylesheet" href="https://fonts.googleapis.com/css2?family=Montserrat:wght@400;700&display=swap">
<style>
  :root {
    --navy: #28306e;
    --navy-deep: #232a62;
    --paper: #ffffff;
    --ink-grey: #7a7d86;
    --backdrop: #e9eaee;
    --card-w: 760px;
    --card-h: 434px;
  }
  * { box-sizing: border-box; margin: 0; padding: 0; }
  html, body {
    width: 1200px; height: 1000px; overflow: hidden;
    background: var(--backdrop);
    font-family: "Montserrat", Arial, sans-serif;
  }
  .sheet {
    width: 1200px; height: 1000px;
    display: flex; flex-direction: column;
    align-items: center; justify-content: center; gap: 44px;
  }
  .card {
    position: relative;
    width: var(--card-w); height: var(--card-h);
    box-shadow: 0 6px 18px rgba(20, 24, 60, 0.18);
    overflow: hidden;
  }
  .company-name {
    font-weight: 700; color: var(--navy);
    white-space: nowrap; line-height: 1.2;
  }
  /* Front */
  .card--front { background: var(--paper); }
  .card--front .company-name {
    position: absolute; top: 56px; right: 52px; font-size: 24px;
  }
  .holder { position: absolute; top: 108px; left: 52px; }
  .holder__name { font-weight: 700; font-size: 21px; color: var(--navy); }
  .holder__role { font-weight: 400; font-size: 15px; color: var(--ink-grey); margin-top: 2px; }
  .contact {
    position: absolute; left: 70px; bottom: 70px;
    list-style: none; font-size: 14px; line-height: 1.62; color: var(--ink-grey);
  }
  .contact__label { display: inline-block; width: 30px; font-weight: 700; color: var(--navy); }
  .band {
    position: absolute; left: 0; right: 0; bottom: 0; height: 48px;
    background: var(--navy);
    display: flex; align-items: center; justify-content: flex-end; padding-right: 28px;
  }
  .band .company-name { font-size: 15px; color: var(--paper); }
  /* Back */
  .card--back {
    background: var(--navy-deep);
    display: flex; align-items: center; justify-content: center;
  }
  .card--back .company-name { color: var(--paper); font-size: 34px; }
</style>
</head>
<body>
  <main class="sheet">
    <section class="card card--front" aria-label="Business card front">
      <p class="company-name">KT &amp; Co Finance Pty Ltd</p>
      <div class="holder">
        <p class="holder__name">Kenneth Tollard</p>
        <p class="holder__role">Managing Director</p>
      </div>
      <ul class="contact">
        <li><span class="contact__label">M :</span>0417 638 294</li>
        <li><span class="contact__label">F :</span>03 9561 2047</li>
        <li><span class="contact__label">E :</span>kenneth.tollard@ktcofinance.example</li>
        <li><span class="contact__label">A :</span>Suite 4/718 Marlow Avenue Ferndale East Vic 3187</li>
        <li><span class="contact__label">CL:</span>382917</li>
      </ul>
      <div class="band"><p class="company-name">KT &amp; Co Finance Pty Ltd</p></div>
    </section>

    <section class="card card--back" aria-label="Business card back">
      <p class="company-name">KT &amp; Co Finance Pty Ltd</p>
    </section>
  </main>
</body>
</html>
```